Lumera Analytics Web Design Project

Web design for a company that highlights the people and experience behind a company that develops solutions, both through the provision of professional services, as well as software development, using mathematical optimisation tools. We want it to be professional looking (minimal bright flashy colors and animation) and allow us to easily update it after delivery without having to purchase any 3rd party software tools. Minimum tabs: About us, services, products, careers, contact. Search box to search site content, including ad-hoc documents add to site (PDF).
The design should emphasis simplicity and professionalism. We need to be able to link documents to the site easily as we add research papers, project descriptions, key personnel resume's etc etc.
Target Market(s)
Technical professionals, researchers, academics
Industry/Entity Type
Software
Look and feel

```html
<!DOCTYPE html>
<html lang="en">
<head>
<meta charset="utf-8">
<title>Lumera Analytics</title>
<link href="https://fonts.googleapis.com/css2?family=Questrial&family=PT+Sans:wght@400;700&display=swap" rel="stylesheet">
<style>
  :root {
    --blue: #0ea1ee;
    --blue-dark: #0a8ad0;
    --red: #e8261b;
    --ink: #222;
    --text: #555;
    --band: #ececec;
    --page: #f8f8f8;
    --frame: #dedede;
    --panel: #e4e5e9;
  }
  * { box-sizing: border-box; margin: 0; padding: 0; }
  html, body { width: 1129px; height: 1200px; overflow: hidden; }
  body {
    position: relative;
    background: var(--page);
    font-family: "PT Sans", sans-serif;
    color: var(--text);
  }
  .abs { position: absolute; }
  .top-band { left: 0; top: 0; width: 1129px; height: 271px; background: var(--band); }
  .footer-band { left: 0; top: 1126px; width: 1129px; height: 74px; background: var(--band); }

  .brand { left: 149px; top: 68px; display: flex; align-items: center; gap: 8px; }
  .brand-dot { width: 16px; height: 16px; border-radius: 50%; background: var(--blue); }
  .brand-name { font-family: "Questrial", sans-serif; font-size: 21px; color: var(--ink); line-height: 1.1; }

  .phone { left: 597px; top: 22px; display: flex; align-items: center; gap: 10px;
    font-family: "Questrial", sans-serif; font-size: 16px; color: #666; }

  .search { left: 782px; top: 16px; width: 198px; height: 34px; display: flex; border: 1px solid #ddd; background: #fff; }
  .search-field { flex: 1; display: flex; align-items: center; justify-content: center;
    font-family: "Questrial", sans-serif; font-size: 14px; color: #aaa; }
  .search-btn { width: 34px; background: var(--blue); display: flex; align-items: center; justify-content: center; }

  .nav-line { left: 408px; top: 68px; width: 605px; height: 33px; border-top: 1px solid #e0e0e0; border-bottom: 1px solid #e0e0e0; }
  .nav { left: 483px; top: 69px; height: 31px; display: flex; list-style: none;
    font-family: "Questrial", sans-serif; font-size: 14.5px; color: var(--ink); }
  .nav li { padding: 0 14px; line-height: 31px; }
  .nav li.active { background: var(--blue); color: #fff; padding: 0 16px; }

  .slider { left: 148px; top: 118px; width: 833px; height: 361px; background: #fff; border: 1px solid var(--frame); }
  .slide-art { left: 155px; top: 125px; width: 819px; height: 347px;
    background: linear-gradient(110deg, #c9dde6 0%, #7fd6df 35%, #a9e6ec 55%, #3f8ad8 80%, #1c4fb8 100%); }
  .slide-dots { left: 874px; top: 440px; width: 100px; height: 32px; background: #fff;
    display: flex; align-items: center; justify-content: center; gap: 8px; }
  .slide-dots span { width: 10px; height: 10px; border-radius: 50%; background: #8d8d8d; }
  .slide-dots span.on { background: var(--red); }

  .section-title { font-family: "Questrial", sans-serif; font-size: 19px; color: var(--ink); font-weight: 400; }
  .feature { top: 502px; width: 261px; }
  .photo-frame { margin-top: 10px; width: 100%; height: 133px; background: #fff; border: 1px solid var(--frame); padding: 4px; }
  .photo-frame div { width: 100%; height: 100%; }
  .copy { font-size: 11px; line-height: 15.6px; text-align: justify; color: var(--text); }
  .feature .copy { margin-top: 11px; }
  .btn-more { width: 75px; height: 23px; background: var(--blue); color: #fff; border-radius: 2px;
    font-family: "Questrial", sans-serif; font-size: 13px; display: flex; align-items: center; justify-content: center; }

  .divider { left: 153px; top: 811px; width: 823px; height: 2px; background: #d4d4d4; }
  .divider::before, .divider::after { content: ""; position: absolute; top: -4px; width: 10px; height: 10px; border-radius: 50%; background: #cfcfcf; }
  .divider::before { left: -5px; } .divider::after { right: -5px; }

  .welcome-photo { left: 148px; top: 853px; width: 261px; height: 134px; background: #fff; border: 1px solid var(--frame); padding: 4px; }
  .welcome-photo div { width: 100%; height: 100%; background: linear-gradient(100deg, #0a2d5a 0%, #1b74c8 40%, #7aa6c9 70%, #dfe6ee 100%); }

  .arrow { width: 21px; height: 20px; border-radius: 3px; display: flex; align-items: center; justify-content: center; }
  .testimonial { left: 721px; top: 855px; width: 260px; height: 144px; background: var(--panel); border-radius: 3px;
    padding: 20px 20px 0 30px; font-size: 11px; line-height: 16.5px; color: #444; }
  .quote-mark { position: absolute; font-family: Georgia, serif; font-size: 16px; color: #555; font-weight: 700; }

  .doc-btn { left: 721px; width: 260px; height: 40px; background: var(--blue); border-radius: 2px;
    display: flex; align-items: center; gap: 24px; padding-left: 12px;
    font-family: "Questrial", sans-serif; font-size: 17px; color: #fff; }

  .footer-links { left: 149px; top: 1145px; font-family: "Questrial", sans-serif; font-size: 12px; color: #777; word-spacing: 2px; }
  .footer-links span { margin: 0 6px; }
  .legal { left: 149px; top: 1165px; font-family: "Questrial", sans-serif; font-size: 12px; color: #777; }
  .social { left: 872px; top: 1148px; display: flex; gap: 8px; }
  .social span { width: 21px; height: 21px; border-radius: 3px; background: var(--blue-dark); }
  .social span:nth-child(3) { background: #2d6fc9; }
  .social span:nth-child(4) { background: #2e5cae; }
</style>
</head>
<body>
  <div class="abs top-band"></div>
  <div class="abs footer-band"></div>

  <header>
    <div class="abs brand">
      <span class="brand-dot"></span>
      <span class="brand-name">Lumera Analytics</span>
    </div>

    <div class="abs phone">
      <svg width="30" height="28" viewBox="0 0 30 28" aria-hidden="true">
        <circle cx="16" cy="14" r="12" fill="none" stroke="#2a8fd6" stroke-width="2"/>
        <path d="M6 6c-3 3-3 9 1 14l3 3c2 1 3 0 4-1l-3-4-2 1c-2-2-3-4-3-7l2-1-1-5z" fill="#2a8fd6"/>
      </svg>
      <span>0800-5550-123</span>
    </div>

    <div class="abs search">
      <div class="search-field">Search</div>
      <div class="search-btn">
        <svg width="12" height="12" viewBox="0 0 12 12" aria-hidden="true">
          <circle cx="5" cy="5" r="3.3" fill="none" stroke="#fff" stroke-width="1.8"/>
          <line x1="7.5" y1="7.5" x2="11" y2="11" stroke="#fff" stroke-width="2"/>
        </svg>
      </div>
    </div>

    <div class="abs nav-line"></div>
    <ul class="abs nav">
      <li class="active">Home</li>
      <li>About Us</li>
      <li>Services</li>
      <li>Products</li>
      <li>Careers</li>
      <li>Contact Us</li>
    </ul>
  </header>

  <section class="abs slider"></section>
  <div class="abs slide-art" role="img" aria-label="Hands drawing with a ruler and pencil over an engineering schematic, a globe and binary digits"></div>
  <div class="abs slide-dots"><span class="on"></span><span></span><span></span><span></span></div>

  <section class="abs feature" style="left:148px">
    <h2 class="section-title">Our Projects</h2>
    <div class="photo-frame"><div role="img" aria-label="Open hand holding a laptop above a glowing world map" style="background:linear-gradient(120deg,#0d1b2a 0%,#1d4f80 45%,#7fb4d8 65%,#0f1e30 100%)"></div></div>
    <p class="copy">Lorem Ipsum is simply dummy text of the printing and typesetting industry. Lorem Ipsum has been the industry's standard dummy text ever since the 1500s, when an unknown printer took a galley of type and scramble</p>
  </section>
  <div class="abs btn-more" style="left:333px;top:766px">More</div>

  <section class="abs feature" style="left:434px">
    <h2 class="section-title">Our Services</h2>
    <div class="photo-frame"><div role="img" aria-label="Businessman writing the word technology on a blue screen" style="background:linear-gradient(100deg,#1b2130 0%,#3a4456 40%,#2f7fc4 75%,#5fb6e8 100%)"></div></div>
    <p class="copy">Lorem Ipsum is simply dummy text of the printing and typesetting industry. Lorem Ipsum has been the industry's standard dummy text ever since the 1500s, when an unknown printer took a galley of type and scramble</p>
  </section>
  <div class="abs btn-more" style="left:618px;top:766px">More</div>

  <section class="abs feature" style="left:721px">
    <h2 class="section-title">Purchase Now</h2>
    <div class="photo-frame"><div role="img" aria-label="Businessman pointing at a glowing globe in a blue digital space" style="background:linear-gradient(110deg,#0a1a3a 0%,#1f5aa8 45%,#4d8fd0 70%,#0f2a55 100%)"></div></div>
    <p class="copy">Lorem Ipsum is simply dummy text of the printing and typesetting industry. Lorem Ipsum has been the industry's standard dummy text ever since the 1500s, when an unknown printer took a galley of type and scramble</p>
  </section>
  <div class="abs btn-more" style="left:906px;top:766px">More</div>

  <div class="abs divider"></div>

  <h2 class="abs section-title" style="left:148px;top:828px">Welcome to Lumera</h2>
  <div class="abs welcome-photo"><div role="img" aria-label="Globe surrounded by a stream of floating photo tiles"></div></div>
  <p class="abs copy" style="left:420px;top:853px;width:273px">Lorem Ipsum is simply dummy text of the printing and typesetting industry. Lorem Ipsum has been the industry's standard dummy text ever since the 1500s, when an unknown printer took a galley of type and scrambleLorem Ipsum is simply dummy text of the printing and typesetting industry. Lorem Ipsum has been the industry's standard dummy text ever since the 1500s, when an unknown printer took a galley of type and scrambled it to make a type specimen book. It has sur-</p>
  <p class="abs copy" style="left:148px;top:993px;width:545px">Lorem Ipsum is simply dummy text of the printing and typesetting industry. Lorem Ipsum has been the industry's standard dummy text ever since the 1500s, when Lorem Ipsum is simply dummy text of the printing and typesetting industry. Lorem Ipsum has been the industry's an unknown printer took a galley of type and scrambled it to Lorem Ipsum passages, and more recently with desktop publishing software like Folio PageSetter including versions of Lorem Ipsum.</p>
  <div class="abs btn-more" style="left:618px;top:1074px">More</div>

  <h2 class="abs section-title" style="left:721px;top:828px">Clients Testimonials</h2>
  <div class="abs arrow" style="left:932px;top:828px;background:var(--red)">
    <svg width="8" height="10" viewBox="0 0 8 10" aria-hidden="true"><path d="M6 1 2 5l4 4" fill="none" stroke="#fff" stroke-width="2"/></svg>
  </div>
  <div class="abs arrow" style="left:961px;top:828px;background:var(--blue)">
    <svg width="8" height="10" viewBox="0 0 8 10" aria-hidden="true"><path d="M2 1l4 4-4 4" fill="none" stroke="#fff" stroke-width="2"/></svg>
  </div>
  <blockquote class="abs testimonial">
    <span class="quote-mark" style="left:16px;top:14px">&ldquo;</span>
    Lorem Ipsum is simply dummy text of the printing and typesetting industry. Lorem Ipsum has been the industry's standard he printing and typesetting industry.dummy text ever since the 1500s, when an unknown printer took <span class="quote-mark" style="position:static;font-size:12px">&rdquo;</span>
  </blockquote>

  <div class="abs doc-btn" style="top:1008px">
    <svg width="36" height="28" viewBox="0 0 36 28" aria-hidden="true">
      <rect x="2" y="4" width="32" height="22" rx="2" fill="#f3d27a"/>
      <rect x="5" y="9" width="20" height="14" fill="#fff"/>
      <path d="M8 13h14M8 17h10" stroke="#aaa" stroke-width="1.5"/>
    </svg>
    <span>Add Documents</span>
  </div>
  <div class="abs doc-btn" style="top:1058px">
    <svg width="36" height="30" viewBox="0 0 36 30" aria-hidden="true">
      <rect x="8" y="3" width="20" height="25" rx="1" fill="#fff" stroke="#ccd" transform="rotate(-8 18 15)"/>
      <path d="M13 10h10M13 14h10M13 18h7" stroke="#9ab" stroke-width="1.5" transform="rotate(-8 18 15)"/>
    </svg>
    <span>key Personnel Resume's</span>
  </div>

  <footer>
    <nav class="abs footer-links">Home<span>|</span>About Us<span>|</span>Services<span>|</span>Products<span>|</span>Add documents<span>|</span>Careers<span>|</span>Contact Us</nav>
    <p class="abs legal">2013@All Right reserved.</p>
    <div class="abs social"><span></span><span></span><span></span><span></span></div>
  </footer>
</body>
</html>
```